Onboarding Carousel UI/UX design

We need a great UI/UX design for our onboarding carousel as attached in the PDF document. The chosen designers will be given our brand book with colors and styles to be used. The images must be focused on the content of each slide and be professional unique style (Do not use the childish cartoons we have used for placeholders)

Industry/Entity Type

Mortgage Brokerage

Number of Pages Required

5+ page

Font styles to use
Other font styles liked:
• Roboto

Requirements
Must have
• Great UI / UX design
Very relevant content of the images to match the slide
Nice to have
• Brand book

https://mock.vexlin.com/view/4b7a21ce-9d05-4f1a-8e63-27c4d90a1b6f-c3d1/?fullscreen

Image styles we like. Would need to be customized and made unique for us.

https://pixmora.com/shots/7418226-Trelvo-Nubank-Illustration-Collaboration
https://kestrelhollowlab.co.za/software-client-style-frames
Should not have
• Do not use the childish images we have used as placeholders

```html
<!DOCTYPE html>
<html lang="en">
<head>
<meta charset="utf-8">
<title>Onboarding – Verify Your Identity Online</title>
<link href="https://fonts.googleapis.com/css2?family=Roboto:wght@400;500;700&display=swap" rel="stylesheet">
<style>
  :root {
    --bg: #ffffff;
    --ink: #132b40;
    --muted: #6b7785;
    --brand: #0963b8;
    --dot: #5aa3e0;
    --art-navy: #1c3550;
    --art-pink: #e0147a;
    --art-olive: #7f8c0c;
    --art-sky: #e6eef6;
  }
  * { box-sizing: border-box; margin: 0; padding: 0; }
  html, body {
    width: 702px;
    height: 1200px;
    overflow: hidden;
    background: var(--bg);
    font-family: "Roboto", Arial, sans-serif;
    color: var(--ink);
  }
  .onboarding {
    position: relative;
    width: 702px;
    height: 1200px;
  }
  .slide-art {
    position: absolute;
    left: 138px;
    top: 133px;
    width: 454px;
    height: 405px;
    border-radius: 28px;
    background: linear-gradient(150deg, var(--art-sky) 0%, #d7e2ee 45%, #c9d3e0 70%, #e9cfe0 100%);
  }
  .slide-title {
    position: absolute;
    left: 0;
    width: 100%;
    top: 668px;
    text-align: center;
    font-size: 39px;
    line-height: 58px;
    color: var(--ink);
  }
  .slide-title strong { font-weight: 700; display: block; }
  .slide-title span { font-weight: 400; display: block; }
  .slide-text {
    position: absolute;
    left: 0;
    width: 100%;
    top: 797px;
    text-align: center;
    font-size: 23px;
    line-height: 39px;
    color: var(--muted);
  }
  .pager {
    position: absolute;
    left: 0;
    width: 100%;
    top: 918px;
    display: flex;
    justify-content: center;
    align-items: center;
    gap: 13px;
  }
  .pager-dot {
    width: 12px;
    height: 12px;
    border-radius: 50%;
    background: var(--dot);
  }
  .pager-dot.is-active {
    width: 20px;
    height: 20px;
    background: var(--brand);
    border: 4px solid var(--bg);
    box-shadow: 0 0 0 2px var(--brand);
  }
  .pager-hint {
    position: absolute;
    left: 0;
    width: 100%;
    top: 954px;
    text-align: center;
    font-size: 17px;
    font-weight: 500;
    color: var(--brand);
  }
  .next-button {
    position: absolute;
    left: 252px;
    top: 1057px;
    width: 198px;
    height: 75px;
    border: 0;
    border-radius: 6px;
    background: var(--brand);
    color: #fff;
    font-family: "Roboto", Arial, sans-serif;
    font-size: 24px;
    font-weight: 700;
  }
  .signin-line {
    position: absolute;
    left: 0;
    width: 100%;
    top: 1150px;
    text-align: center;
    font-size: 20px;
    color: var(--ink);
  }
  .signin-line a { color: var(--brand); text-decoration: none; margin-left: 6px; }
</style>
</head>
<body>
  <main class="onboarding">
    <div class="slide-art" role="img" aria-label="Illustration of a woman reclining and holding a phone beside a Romanian ID card with a shield and check mark"></div>

    <h1 class="slide-title">
      <strong>#3 Verify Your</strong>
      <span>Identity Online</span>
    </h1>

    <p class="slide-text">You will need to have a valid<br>Romanian ID card or residence permit</p>

    <div class="pager" aria-label="Slide 3 of 5">
      <span class="pager-dot is-active"></span>
      <span class="pager-dot"></span>
      <span class="pager-dot"></span>
      <span class="pager-dot"></span>
      <span class="pager-dot"></span>
    </div>
    <p class="pager-hint">You will take a photo of your card</p>

    <button class="next-button" type="button">Next</button>
    <p class="signin-line">Have an Account?<a href="#">Sign In</a></p>
  </main>
</body>
</html>
```